We are looking to recreate our Harlow & Partners Jobsite Sign. This sign will be placed by the street at each of our jobsites. We want to keep this sign simple, but at the same time, want to add a catching appeal to the design for anyone passing by. We want to stick to a two color scheme (Harlow Blue, and White). Please only use the Company Logo that I have uploaded for this project. Please also see a mock up of what we would like to include on this sign. The Sign Dimensions will be 4' x 8'. Please keep all verbiage uniform with the verbiage on the sample design I have uploaded. LET YOUR CREATIVITY FLOW!

```html
<!DOCTYPE html>
<html lang="en">
<head>
<meta charset="utf-8">
<title>Harlow &amp; Partners Jobsite Sign</title>
<link href="https://fonts.googleapis.com/css2?family=Bitter:wght@700&display=swap" rel="stylesheet">
<style>
  :root {
    --harlow-blue: #1a1a96;
    --white: #ffffff;
    --backdrop: #4a4a4a;
  }
  html, body {
    margin: 0;
    padding: 0;
    width: 957px;
    height: 1200px;
    overflow: hidden;
    background: var(--backdrop);
  }
  .jobsite-sign {
    position: absolute;
    left: 90px;
    top: 406px;
    width: 973px;
    height: 485px;
    transform: scale(0.7975);
    transform-origin: 0 0;
    font-family: "Bitter", Georgia, serif;
    font-weight: 700;
    box-shadow: 6px 8px 14px rgba(0,0,0,0.45);
    background: var(--white);
  }
  .sign-shape { position: absolute; left: 0; top: 0; }
  .company-name {
    position: absolute;
    left: 96px;
    top: 84px;
    width: 350px;
    color: var(--white);
    text-align: center;
    line-height: 1;
  }
  .company-name .name-main { display: block; font-size: 86px; letter-spacing: -1px; }
  .company-name .name-sub { display: block; font-size: 38px; margin-top: 2px; }
  .trade {
    position: absolute;
    left: 515px;
    top: 92px;
    width: 366px;
    color: var(--white);
    text-align: center;
    font-size: 54px;
    line-height: 1.02;
  }
  .tagline {
    position: absolute;
    left: 0;
    top: 222px;
    width: 973px;
    color: var(--white);
    text-align: center;
    font-size: 48px;
    line-height: 60px;
    letter-spacing: -0.3px;
  }
  .location {
    position: absolute;
    left: 295px;
    top: 351px;
    width: 381px;
    height: 56px;
    line-height: 56px;
    color: var(--white);
    text-align: center;
    font-size: 36px;
  }
  .contact-line {
    position: absolute;
    left: 33px;
    top: 423px;
    width: 906px;
    height: 48px;
    display: flex;
    justify-content: space-evenly;
    align-items: center;
    color: var(--harlow-blue);
    font-size: 32px;
  }
  .contact-line .separator {
    width: 3px;
    height: 40px;
    background: var(--harlow-blue);
  }
</style>
</head>
<body>
  <div class="jobsite-sign">
    <svg class="sign-shape" viewBox="0 0 973 485" width="973" height="485" aria-hidden="true">
      <rect x="0" y="390" width="33" height="95" fill="var(--harlow-blue)"/>
      <rect x="940" y="390" width="33" height="95" fill="var(--harlow-blue)"/>
      <rect x="295" y="330" width="381" height="77" rx="8" fill="var(--harlow-blue)"/>
      <polygon points="0,370 486,322 973,370 973,392 486,342 0,392" fill="var(--white)"/>
      <polygon points="12,14 486,72 961,14 961,368 486,322 12,370" fill="var(--harlow-blue)"/>
      <rect x="484" y="102" width="4" height="110" fill="var(--white)"/>
    </svg>

    <div class="company-name">
      <span class="name-main">Harlow</span>
      <span class="name-sub">&amp; Partners, Inc.</span>
    </div>
    <div class="trade">General<br>Contractors</div>
    <div class="tagline">“Building Trust On Every Job”</div>
    <div class="location">Lakemont, Florida</div>
    <div class="contact-line">
      <span class="phone">407-555-0142</span>
      <span class="separator"></span>
      <span class="web">HarlowPartners.net</span>
      <span class="separator"></span>
      <span class="license">CGC1048821</span>
    </div>
  </div>
</body>
</html>
```